Candy Packaging

I'm looking for a logo design for a confectionary company called Nana's Sweet Delights.
Something that will be appealing to women.
The packaging in interested in will be a stand up guseted bag with a window.
Dimensions ar 7 1/2in high, 4in wide 2in thick.

Im trying to upload pictures of the product and I'm not sure if the're loading.

Target Market(s)

Adult Females

Industry/Entity Type

It Company

```html
<!DOCTYPE html>
<html lang="en">
<head>
<meta charset="utf-8">
<title>Nana's Sweet Delights – Colored Balls Bag</title>
<link rel="stylesheet" href="https://fonts.googleapis.com/css2?family=Oswald:wght@400;500&family=Yellowtail&display=swap">
<style>
  :root {
    --backdrop: #6e4c4c;
    --bag: #e05254;
    --bag-shade: #d4464a;
    --band: #8c2f35;
    --burst: #c8163f;
    --burst-edge: #a80f33;
    --cream: #fbeaa0;
    --title: #f6e27a;
    --white: #ffffff;
    --candy-pink: #e8679a;
    --candy-orange: #f29a3c;
    --candy-yellow: #efe15a;
    --candy-green: #3fb863;
  }
  * { margin: 0; padding: 0; box-sizing: border-box; }
  html, body { width: 1041px; height: 1200px; overflow: hidden; background: var(--backdrop); }
  .canvas { position: relative; width: 1041px; height: 1200px; overflow: hidden; }
  .bag-art { position: absolute; inset: 0; }
  .brand {
    position: absolute; left: 221px; width: 589px; top: 300px;
    text-align: center; color: var(--white);
    font-family: "Oswald", sans-serif; font-weight: 500;
    font-size: 40px; line-height: 1.15; letter-spacing: 1px; text-transform: uppercase;
  }
  .burst-text {
    position: absolute; left: 662px; width: 120px; top: 388px;
    text-align: center; color: #ffd9de;
    font-family: "Oswald", sans-serif; font-weight: 500;
    font-size: 20px; line-height: 21px; text-transform: uppercase;
  }
  .product-name {
    position: absolute; left: 300px; top: 490px; width: 360px;
    text-align: center; color: var(--title);
    font-family: "Yellowtail", cursive; font-size: 62px;
    transform: rotate(-11deg); transform-origin: center;
    text-shadow: 1px 2px 0 rgba(120, 30, 35, .35);
  }
  .claims {
    position: absolute; left: 266px; top: 924px; list-style: none;
    font-family: "Oswald", sans-serif; font-weight: 400;
    font-size: 16px; line-height: 21px; color: var(--cream); text-transform: uppercase;
  }
  .claims li { display: flex; align-items: center; gap: 10px; }
  .claims svg { width: 15px; height: 15px; fill: var(--cream); }
  .net-weight {
    position: absolute; left: 722px; top: 962px;
    font-family: "Oswald", sans-serif; font-weight: 500;
    font-size: 21px; color: #f7dcdc;
  }
</style>
</head>
<body>
<main class="canvas">
  <svg class="bag-art" width="1041" height="1200" viewBox="0 0 1041 1200" aria-hidden="false">
    <defs>
      <pattern id="seal-teeth" x="221" y="135" width="12" height="9" patternUnits="userSpaceOnUse">
        <polygon points="0,9 6,0 12,9" fill="var(--bag)"/>
      </pattern>
      <linearGradient id="bag-body" x1="0" y1="0" x2="1" y2="0">
        <stop offset="0" stop-color="var(--bag-shade)"/>
        <stop offset="0.12" stop-color="var(--bag)"/>
        <stop offset="0.88" stop-color="var(--bag)"/>
        <stop offset="1" stop-color="var(--bag-shade)"/>
      </linearGradient>
      <linearGradient id="candy-fill" x1="0" y1="0" x2="1" y2="1">
        <stop offset="0" stop-color="var(--candy-orange)"/>
        <stop offset="0.3" stop-color="var(--candy-pink)"/>
        <stop offset="0.55" stop-color="var(--candy-yellow)"/>
        <stop offset="0.75" stop-color="var(--candy-green)"/>
        <stop offset="1" stop-color="var(--candy-pink)"/>
      </linearGradient>
    </defs>

    <g class="bag">
      <rect class="bag-seal" x="221" y="135" width="589" height="9" fill="url(#seal-teeth)"/>
      <rect class="bag-body" x="221" y="143" width="589" height="895" fill="url(#bag-body)"/>
    </g>

    <path class="band band-upper" d="M221,650 C400,602 650,545 810,522 L810,547 C650,568 400,626 221,674 Z" fill="var(--band)"/>
    <path class="band band-lower" d="M221,800 C400,862 650,900 810,905 L810,930 C650,926 400,886 221,826 Z" fill="var(--band)"/>

    <g class="window" role="img" aria-label="Window showing a pile of colourful candy balls in pink, orange, yellow and green">
      <path d="M268,735 C258,640 420,602 620,577 C762,560 792,622 776,720 C760,822 700,872 560,866 C420,860 278,830 268,735 Z"
            fill="url(#candy-fill)" stroke="var(--band)" stroke-width="10"/>
    </g>

    <polygon class="burst" fill="var(--burst)" stroke="var(--burst-edge)" stroke-width="3"
      points="790,419 772,432 781,453 759,456 756,478 735,469 722,487 709,469 688,478 685,456 663,453 672,432 654,419 672,406 663,385 685,382 688,360 709,369 722,351 735,369 756,360 759,382 781,385 772,406"/>
  </svg>

  <div class="brand">Nana's<br>Sweet Delights</div>
  <div class="burst-text">Taste<br>Like<br>Home</div>
  <h1 class="product-name">Colored Balls</h1>

  <ul class="claims">
    <li><svg viewBox="0 0 24 24"><polygon points="12,1 15,9 23,9 17,14 19,23 12,18 5,23 7,14 1,9 9,9"/></svg>Less Sugar</li>
    <li><svg viewBox="0 0 24 24"><polygon points="12,1 15,9 23,9 17,14 19,23 12,18 5,23 7,14 1,9 9,9"/></svg>No Artificial Taste</li>
    <li><svg viewBox="0 0 24 24"><polygon points="12,1 15,9 23,9 17,14 19,23 12,18 5,23 7,14 1,9 9,9"/></svg>No Additives</li>
  </ul>
  <div class="net-weight">500g</div>
</main>
</body>
</html>
```